4D Hush Little Nest Luxury Ultrasound Billboard

Design a HIGH-END, MODERN billboard for my private prenatal ultrasound studio, 4D Hush Little Nest, located in Pace, Florida.
This billboard will be viewed by drivers traveling at highway speeds, so it must be extremely clean, simple, and readable within 6 seconds.
About My Business
4D Hush Little Nest is a private prenatal ultrasound studio specializing in:
Highest technology 4D/HD Ultrasounds
Early Gender Determination
Pregnancy Confirmation
I have been serving families for nearly 10 years and is known for creating a memorable experience, not just an ultrasound appointment.
Design Style
I DO NOT want:
Flowers
Leaves
Swirls
Glitter
Hearts everywhere
Busy backgrounds
Generic maternity stock graphics
I DO want:
Modern
Luxury
Upscale
Clean
Professional
Eye-catching
Premium medical spa feel
Colors
Use colors from my logo:
LOGO Green ( or a deep green)
Black
White
Soft Gold accents
Images:
Incorporate my professional headshot in a clean, modern way, logo, and the ultrasound images
Text
Keep wording minimal.
Primary Headline ( OPEN TO IDEAS) :
EXAMPLES ( WOULD RATHER SOMETHING MORE CATCHY)
" ADVANCED IMAGING. UNFORGETTABLE MOMENTS"
"MEET YOUR BABY BEFORE BIRTH"
Under headline:
4D Ultrasound • Early Gender • Pregnancy Confirmation
Business Name:
4D Hush Little Nest
Private Prenatal Ultrasound Studio
Phone Number:
850-471-3905
Important
This billboard must be readable in 5–6 seconds from a moving vehicle.
Less text is better.
The phone number and business name must be visible from a distance.
The design should feel like a premium brand that immediately tells expecting parents:
“This is where I go to see my baby.”
Files Provided
Official logo
Headshot
Ultrasound images
Don’t make this look like a medical office billboard.
Make it look like a luxury baby experience billboard. That’s what separates 4D Hush Little Nest from hospitals, OB offices, and all the new studios popping up around you. The emotional connection is what gets moms to book. ❤️
Billboard Size - 10.6” x 36”

```html
<!DOCTYPE html>
<html lang="en">
<head>
<meta charset="utf-8">
<title>4D Hush Little Nest Billboard</title>
<link href="https://fonts.googleapis.com/css2?family=Playfair+Display:wght@700&family=Poppins:wght@400;500;600&display=swap" rel="stylesheet">
<style>
  :root {
    --stage: #c2c2c2;
    --ink: #1e1e1e;
    --deep-green: #2c3530;
    --gold: #c9a04a;
    --gold-light: #ecc978;
    --gold-dark: #a67a2c;
    --white: #ffffff;
    --slate: #56625d;
    --skin-light: #b97a57;
    --skin-dark: #6e3a22;
  }
  * { margin: 0; padding: 0; box-sizing: border-box; }
  html, body { width: 1105px; height: 1200px; overflow: hidden; background: var(--stage); }
  body { position: relative; font-family: "Poppins", sans-serif; }

  .billboard {
    position: absolute; left: 40px; top: 344px;
    width: 1025px; height: 512px;
    background: var(--ink); overflow: hidden;
  }
  .contact-band {
    position: absolute; left: 0; top: 390px; width: 100%; height: 122px;
    background: var(--deep-green); border-top: 2px solid var(--gold);
  }
  .headshot {
    position: absolute; left: 21px; top: 14px; width: 247px; height: 345px;
    border-radius: 120px 120px 0 0;
    background: linear-gradient(180deg, #d8bd8c 0%, #a98a5e 35%, #2f4a32 70%, #e6e6e6 100%);
  }
  .ultrasound-art { position: absolute; left: 0; top: 0; width: 1025px; height: 392px; }

  .headline { position: absolute; left: 312px; width: 400px; text-align: center; color: var(--white); }
  .headline-top { top: 28px; font-size: 44px; font-weight: 500; letter-spacing: 4px; line-height: 1; }
  .headline-main {
    top: 68px; font-family: "Playfair Display", serif; font-weight: 700;
    font-size: 132px; line-height: 1; letter-spacing: 2px;
    background: linear-gradient(180deg, var(--gold-light) 0%, var(--gold) 50%, var(--gold-dark) 100%);
    -webkit-background-clip: text; background-clip: text; color: transparent;
  }
  .headline-bottom { top: 186px; font-size: 44px; font-weight: 500; letter-spacing: 4px; line-height: 1; }

  .divider {
    position: absolute; left: 343px; top: 255px; width: 339px; height: 2px;
    background: linear-gradient(90deg, transparent, var(--gold) 50%, transparent);
  }
  .divider::after {
    content: ""; position: absolute; left: 50%; top: -2px; width: 6px; height: 6px;
    margin-left: -3px; border-radius: 50%; background: var(--gold-light);
  }

  .service { position: absolute; top: 292px; width: 140px; text-align: center; color: var(--white); }
  .service svg { display: block; margin: 0 auto 6px; }
  .service-label { font-size: 12.5px; font-weight: 500; letter-spacing: 0.5px; line-height: 1.15; }
  .service-sep { position: absolute; top: 295px; width: 1px; height: 64px; background: #8a8a8a; }

  .logo-card {
    position: absolute; left: 19px; top: 357px; width: 266px; height: 134px;
    background: var(--white); border: 2px solid #7a8581; border-radius: 14px;
    display: flex; flex-direction: column; align-items: center; justify-content: center;
  }
  .logo-name { font-size: 24px; font-weight: 600; color: var(--gold); line-height: 1.2; text-align: center; }
  .logo-rule { width: 235px; height: 1px; background: var(--gold); margin: 12px 0 10px; }
  .logo-tagline { font-size: 10.5px; font-weight: 500; color: var(--slate); letter-spacing: 0.6px; }

  .phone-icon { position: absolute; left: 326px; top: 429px; }
  .phone-number {
    position: absolute; left: 378px; top: 421px; font-size: 42px; font-weight: 600;
    color: var(--white); letter-spacing: 1px; line-height: 1.3;
  }
  .contact-sep { position: absolute; left: 728px; top: 428px; width: 1px; height: 46px; background: #8a8a8a; }
  .tagline {
    position: absolute; left: 748px; top: 425px; width: 262px; text-align: center;
    font-size: 21px; font-weight: 400; color: var(--gold-light); line-height: 1.15; letter-spacing: 0.5px;
  }
</style>
</head>
<body>
<main class="billboard">
  <div class="contact-band"></div>

  <svg class="ultrasound-art" viewBox="0 0 1025 392" role="img" aria-label="4D ultrasound image of a baby's face in warm amber tones">
    <defs>
      <linearGradient id="scanTone" x1="0" y1="0" x2="1" y2="1">
        <stop offset="0" stop-color="#c08562"/>
        <stop offset="0.55" stop-color="#8f4d2c"/>
        <stop offset="1" stop-color="#5a2c18"/>
      </linearGradient>
      <linearGradient id="goldEdge" x1="0" y1="0" x2="0" y2="1">
        <stop offset="0" stop-color="#d7ad5a"/>
        <stop offset="0.5" stop-color="#f2d389"/>
        <stop offset="1" stop-color="#b8893a"/>
      </linearGradient>
    </defs>
    <path d="M822 0 L752 290 Q740 345 780 390 L1025 390 L1025 0 Z" fill="url(#goldEdge)"/>
    <path d="M832 0 L764 290 Q753 343 792 390 L1025 390 L1025 0 Z" fill="url(#scanTone)"/>
  </svg>

  <div class="headshot" role="img" aria-label="Professional headshot of the studio owner holding an ultrasound probe"></div>

  <div class="headline headline-top">MEET YOUR</div>
  <div class="headline headline-main">BABY</div>
  <div class="headline headline-bottom">BEFORE BIRTH</div>
  <div class="divider"></div>

  <div class="service" style="left:299px">
    <svg width="28" height="44" viewBox="0 0 28 44" fill="none" stroke="var(--gold)" stroke-width="1.6" stroke-linecap="round">
      <path d="M6 6 Q14 0 22 6"/><path d="M9 10 Q14 6 19 10"/>
      <path d="M7 14 H21 V22 Q21 26 18 28 L17 36 H11 L10 28 Q7 26 7 22 Z"/>
      <path d="M14 36 Q14 42 22 40"/>
    </svg>
    <div class="service-label">4D ULTRASOUND</div>
  </div>
  <div class="service-sep" style="left:446px"></div>
  <div class="service" style="left:447px">
    <svg width="44" height="44" viewBox="0 0 44 44" fill="none" stroke="var(--gold)" stroke-width="2" stroke-linecap="round">
      <circle cx="14" cy="22" r="8"/><path d="M14 30 V40 M9 35 H19"/>
      <circle cx="24" cy="18" r="8"/><path d="M30 12 L38 4 M32 4 H38 V10"/>
    </svg>
    <div class="service-label">EARLY GENDER</div>
  </div>
  <div class="service-sep" style="left:587px"></div>
  <div class="service" style="left:591px">
    <svg width="44" height="44" viewBox="0 0 44 44" fill="none" stroke="var(--gold)" stroke-width="1.6" stroke-linecap="round" stroke-linejoin="round">
      <circle cx="22" cy="22" r="19"/><path d="M15 22 L20 27 L29 17" stroke-width="2.4"/>
    </svg>
    <div class="service-label">PREGNANCY<br>CONFIRMATION</div>
  </div>

  <div class="logo-card">
    <div class="logo-name">4D Hush Little Nest</div>
    <div class="logo-rule"></div>
    <div class="logo-tagline">PRENATAL ULTRASOUND STUDIO</div>
  </div>

  <svg class="phone-icon" width="40" height="40" viewBox="0 0 40 40">
    <circle cx="20" cy="20" r="18" fill="none" stroke="var(--gold)" stroke-width="2"/>
    <path d="M13 11 L17 11 L18.5 16 L16 18 Q18 23 22 24.5 L24 22 L29 23.5 L29 27.5 Q27 30 23 29 Q13 26 11 16 Q11 12 13 11 Z" fill="var(--gold)"/>
  </svg>
  <div class="phone-number">850-471-3905</div>
  <div class="contact-sep"></div>
  <div class="tagline">PRECIOUS MOMENTS<br>LIFETIME MEMORIES</div>
</main>
</body>
</html>
```